SOC audit and security advisory company

We are a small public accounting firm that specializes in SOC attestations for small to medium sized business throughout the U.S. Our business is much like consulting, but we form an opinion about their operational controls. We are looking for "relevance and with a hint of polished sophistication". Our logo colors are dark gray and red. Our existing site is www.veltrocheck.com for detailed information. We would like to include some type of captcha if possible. This is an information only site.

Target Market(s)

Small to medium sized financial and IT audit companies that are innovative and flexible.

Industry/Entity Type

Auditing

Coding

Coded - Design and coding required

Number of Pages Required

4 page

Font styles to use
Sans Serif

Requirements
Must have
• Good flow and attention to the content.
Nice to have
• CAPTCHA for contact us page
Should not have
• Big Bold lines.
• Too many distractions.

```html
<!DOCTYPE html>
<html lang="en">
<head>
<meta charset="utf-8">
<title>Veltro – SOC Audit &amp; Security Advisory</title>
<link rel="stylesheet" href="https://fonts.googleapis.com/css2?family=Raleway:wght@500;600;700&family=Open+Sans:ital,wght@0,400;0,600;1,400&display=swap">
<style>
:root{
  --red:#e3222f;
  --red-band:#e9505a;
  --orange:#f08a24;
  --green:#6aae45;
  --ink:#2b2b2b;
  --text:#555;
  --muted:#8a8a8a;
  --white:#fff;
  --dark:#2e3033;
  --line:#e3e3e3;
}
*{margin:0;padding:0;box-sizing:border-box}
html,body{width:678px;height:1200px;overflow:hidden;background:var(--white)}
body{position:relative;font-family:"Open Sans",sans-serif;color:var(--text)}
.abs{position:absolute}
.head-font{font-family:"Raleway",sans-serif}

/* header */
.site-header{left:0;top:0;width:678px;height:50px;background:var(--white)}
.brand{left:56px;top:13px;font:600 22px/1 "Raleway",sans-serif;color:var(--ink);letter-spacing:.5px}
.brand-sub{left:57px;top:36px;font:500 5px/1 "Raleway",sans-serif;color:var(--ink);letter-spacing:1px}
.nav{top:22px;font:600 7px/1 "Raleway",sans-serif;color:var(--ink);letter-spacing:.2px}
.nav.active{color:var(--red)}

/* hero */
.hero{left:0;top:50px;width:678px;height:245px;background:linear-gradient(120deg,#6d6d6d 0%,#8a8a8a 40%,#5b5b5b 100%)}
.hero-brand{left:0;width:678px;top:58px;text-align:center;font:500 30px/1 "Raleway",sans-serif;color:var(--white);letter-spacing:1px}
.hero-title{left:0;width:678px;top:100px;text-align:center;font:600 24px/1 "Raleway",sans-serif;color:var(--white)}
.btn-red{background:var(--red);color:var(--white);border:2px solid var(--white);font:700 8px/1 "Raleway",sans-serif;display:flex;align-items:center;justify-content:center;border-radius:3px}
.hero-btn{left:290px;top:140px;width:98px;height:30px}
.slider-dots{left:630px;top:88px}

/* pillars */
.pillar-img{width:82px;height:82px;border-radius:50%;border:3px solid var(--white);box-shadow:0 0 0 1px var(--line);background:radial-gradient(circle at 45% 45%,#f1e3cf,#c9b08d 70%,#9c8466)}
.pillar-label{width:120px;text-align:center;font:600 8px/1 "Raleway",sans-serif;color:var(--ink)}

/* welcome */
.welcome-title{left:56px;top:388px;font:600 12px/1 "Raleway",sans-serif;color:var(--ink)}
.mission{left:56px;top:411px;font:italic 400 7px/1 "Open Sans",sans-serif;color:var(--red)}
.welcome-body{left:56px;top:432px;width:310px;font-size:6.6px;line-height:16.4px;color:var(--text)}
.read-more{left:56px;top:507px;font:700 7px/1 "Raleway",sans-serif;color:var(--red)}

/* why band */
.why{left:0;top:554px;width:678px;height:228px;background:linear-gradient(180deg,#ea5a63,#e4464f)}
.why-title{left:0;width:678px;top:22px;text-align:center;font:600 12px/1 "Raleway",sans-serif;color:var(--white)}
.why-text{left:130px;width:418px;top:46px;text-align:center;font-size:6.8px;line-height:13.5px;color:var(--white)}
.feature-label{width:140px;text-align:center;font:600 8px/1 "Raleway",sans-serif;color:var(--white);top:92px}
.feature-rule{width:1.5px;height:24px;background:var(--white);top:109px}
.feature-icon{width:62px;height:62px;border:1.5px solid var(--white);border-radius:50%;top:143px;display:flex;align-items:center;justify-content:center}

/* testimonial */
.quote-mark{left:86px;top:811px;width:62px;height:62px;border-radius:50%;background:#e6e6e6;font:700 40px/62px "Raleway",sans-serif;color:#c9c9c9;text-align:center;padding-right:14px}
.avatar{left:127px;top:811px;width:62px;height:62px;border-radius:50%;background:linear-gradient(160deg,#cfd4da,#6c7480);border:2px solid var(--white)}
.quote-text{left:206px;top:812px;width:384px;font:italic 400 6.8px/15.3px "Open Sans",sans-serif;color:var(--text)}
.quote-name{left:206px;top:869px;font:600 8.5px/1 "Open Sans",sans-serif;color:var(--ink)}
.arrow{top:832px}

/* contact */
.contact{left:0;top:907px;width:678px;height:251px;background:linear-gradient(180deg,#3b3d40,#2a2c2f)}
.contact-title{left:0;width:678px;top:23px;text-align:center;font:600 12px/1 "Raleway",sans-serif;color:var(--white)}
.sub-title{font:600 8.5px/1 "Raleway",sans-serif;color:var(--white)}
.field{left:56px;width:356px;background:var(--white);border:1px solid #ccc;font-size:6px;color:#777;padding:6px 8px;letter-spacing:.3px}
.submit{left:358px;top:197px;width:54px;height:25px}
.info-icon{left:457px;width:22px;height:22px;border:1.3px solid var(--white);border-radius:50%;display:flex;align-items:center;justify-content:center}
.info-text{left:503px;font-size:6.6px;line-height:13.5px;color:var(--white)}
.social-box{top:206px;width:15px;height:15px;background:var(--white);border-radius:2px}

/* footer */
.copyright{left:0;width:678px;top:1175px;text-align:center;font-size:6.4px;color:var(--muted)}
</style>
</head>
<body>

<header class="abs site-header">
  <div class="abs brand">VELTRO</div>
  <div class="abs brand-sub">AUDIT &amp; ADVISORY</div>
  <div class="abs nav active" style="left:314px">HOME</div>
  <div class="abs nav" style="left:353px">SOC AND ADVISORY SERVICES</div>
  <div class="abs nav" style="left:478px">ABOUT US</div>
  <div class="abs nav" style="left:532px">CONTACT US</div>
  <svg class="abs" style="left:596px;top:21px" width="9" height="9" viewBox="0 0 10 10"><circle cx="4" cy="4" r="3" fill="none" stroke="#2b2b2b" stroke-width="1.6"/><line x1="6.2" y1="6.2" x2="9" y2="9" stroke="#2b2b2b" stroke-width="1.8"/></svg>
</header>

<section class="abs hero" role="img" aria-label="Photo of a hand with a pen over financial charts on a desk">
  <div class="abs hero-brand">VELTRO</div>
  <h1 class="abs hero-title">SOC Audit &amp; Security Advisory</h1>
  <div class="abs btn-red hero-btn">GET STARTED</div>
  <svg class="abs slider-dots" width="12" height="70" viewBox="0 0 12 70">
    <polyline points="2,6 6,2 10,6" fill="none" stroke="#fff" stroke-width="1.3"/>
    <circle cx="6" cy="18" r="3.6" fill="#e3222f" stroke="#fff" stroke-width="1"/>
    <circle cx="6" cy="28" r="3.6" fill="none" stroke="#fff" stroke-width="1"/>
    <circle cx="6" cy="38" r="3.6" fill="none" stroke="#fff" stroke-width="1"/>
    <circle cx="6" cy="48" r="3.6" fill="none" stroke="#fff" stroke-width="1"/>
    <polyline points="2,60 6,64 10,60" fill="none" stroke="#fff" stroke-width="1.3"/>
  </svg>
</section>

<div class="abs pillar-img" style="left:56px;top:253px" role="img" aria-label="Photo of a hand stacking wooden blocks"></div>
<div class="abs pillar-img" style="left:176px;top:253px" role="img" aria-label="Photo of a hand stopping falling dominoes"></div>
<div class="abs pillar-img" style="left:295px;top:253px" role="img" aria-label="Photo of wooden blocks with people icons"></div>
<div class="abs pillar-label" style="left:37px;top:345px">QUALITY</div>
<div class="abs pillar-label" style="left:157px;top:345px">RISK</div>
<div class="abs pillar-label" style="left:276px;top:345px">MANAGEMENT</div>

<svg class="abs" style="left:403px;top:313px" width="220" height="220" viewBox="-110 -110 220 220">
  <circle r="108" fill="#fff" stroke="#e0e0e0" stroke-width="1.5"/>
  <path d="M0 0 L0 -104 A104 104 0 0 1 90.07 52 Z" fill="#f08a24" stroke="#fff" stroke-width="3"/>
  <path d="M0 0 L90.07 52 A104 104 0 0 1 -90.07 52 Z" fill="#6aae45" stroke="#fff" stroke-width="3"/>
  <path d="M0 0 L-90.07 52 A104 104 0 0 1 0 -104 Z" fill="#e3222f" stroke="#fff" stroke-width="3"/>
  <rect x="-37" y="-38" width="74" height="72" rx="4" fill="#fff" stroke="#bbb" stroke-width="1.5"/>
  <text x="0" y="6" text-anchor="middle" font-family="Raleway,sans-serif" font-weight="700" font-size="17" fill="#2b2b2b">AUDIT</text>
  <text x="0" y="0" transform="translate(-52,-30) rotate(-62)" text-anchor="middle" font-family="Raleway,sans-serif" font-weight="600" font-size="11" fill="#fff">QUALITY</text>
  <text x="0" y="0" transform="translate(58,-28) rotate(55)" text-anchor="middle" font-family="Raleway,sans-serif" font-weight="600" font-size="11" fill="#fff">MANAGEMENT</text>
  <text x="0" y="75" text-anchor="middle" font-family="Raleway,sans-serif" font-weight="600" font-size="11" fill="#fff">RISK</text>
</svg>

<h2 class="abs welcome-title">WELCOME TO VELTRO</h2>
<p class="abs mission">Our mission is to educate and provide high quality services through long term client relationships.</p>
<p class="abs welcome-body">Veltro was established to provide boutique audit and advisoy services to small to medium sized businesses. We know that every company is different. We take a consultitive approach to engaging our clients so they fully understand the process and get something more than just a report! Our clients gain knowledge!</p>
<div class="abs read-more">READ MORE &gt;&gt;</div>

<section class="abs why" role="img" aria-label="Red tinted photo of wooden blocks with people icons">
  <h2 class="abs why-title">WHY CHOOSE VELTRO?</h2>
  <p class="abs why-text">Our proven implementation and audit models allow for capturing requirements while expiditing the process.Our professionals maintain certifications required for your service needs. We utilize the best so you get the best results.</p>

  <div class="abs feature-label" style="left:78px">FREE CONSULTATION</div>
  <div class="abs feature-label" style="left:269px">FIXED COST</div>
  <div class="abs feature-label" style="left:457px">RESULTS DRIVEN</div>
  <div class="abs feature-rule" style="left:148px"></div>
  <div class="abs feature-rule" style="left:339px"></div>
  <div class="abs feature-rule" style="left:527px"></div>

  <div class="abs feature-icon" style="left:117px">
    <svg width="28" height="22" viewBox="0 0 28 22" fill="none" stroke="#fff" stroke-width="2">
      <ellipse cx="11" cy="8" rx="9" ry="6"/><path d="M5 13 L3 18 L9 14"/>
      <path d="M19 7 C24 8 26 11 25 14 C24 16 22 17 20 17 L23 21 L16 17 C13 17 11 16 10 15"/>
    </svg>
  </div>
  <div class="abs feature-icon" style="left:308px">
    <svg width="24" height="24" viewBox="0 0 24 24"><path d="M3 3 H12 L22 13 L13 22 L3 12 Z" fill="#fff"/><circle cx="7.5" cy="7.5" r="2" fill="#e4464f"/></svg>
  </div>
  <div class="abs feature-icon" style="left:496px">
    <svg width="26" height="22" viewBox="0 0 26 22" fill="#fff"><rect x="3" y="9" width="3" height="10"/><rect x="8" y="12" width="3" height="7"/><rect x="13" y="6" width="3" height="13"/><rect x="18" y="3" width="3" height="16"/><rect x="1" y="20" width="24" height="1.5"/></svg>
  </div>
</section>

<svg class="abs arrow" style="left:56px" width="10" height="16" viewBox="0 0 10 16"><polyline points="8,1 2,8 8,15" fill="none" stroke="#b5b5b5" stroke-width="1.8"/></svg>
<svg class="abs arrow" style="left:612px" width="10" height="16" viewBox="0 0 10 16"><polyline points="2,1 8,8 2,15" fill="none" stroke="#b5b5b5" stroke-width="1.8"/></svg>
<div class="abs quote-mark">&ldquo;</div>
<div class="abs avatar" role="img" aria-label="Portrait photo of the client"></div>
<p class="abs quote-text">It is a long established fact that a reader will be distracted by the readable content of a page when looking at its layout. The point of using Lorem Ipsum is that it has a more-or-less normal distribution of letters, as opposed to using 'Content here, content here', making it look like readable English.</p>
<div class="abs quote-name">- Daniel Reeves</div>

<section class="abs contact" role="img" aria-label="Dark photo of a city skyline">
  <h2 class="abs contact-title">CONTACT US</h2>
  <div class="abs sub-title" style="left:56px;top:64px">CONTACT FORM</div>
  <div class="abs field" style="top:88px;height:19px">NAME :</div>
  <div class="abs field" style="top:114px;height:19px">EMAIL :</div>
  <div class="abs field" style="top:141px;height:46px">MESSAGE :</div>
  <div class="abs btn-red submit">SUBMIT</div>

  <div class="abs sub-title" style="left:457px;top:62px">CONTACT INFORMATION</div>
  <div class="abs info-icon" style="top:83px">
    <svg width="9" height="12" viewBox="0 0 9 12"><path d="M4.5 0 C7 0 9 2 9 4.5 C9 7.5 4.5 12 4.5 12 C4.5 12 0 7.5 0 4.5 C0 2 2 0 4.5 0 Z" fill="#fff"/><circle cx="4.5" cy="4.5" r="1.6" fill="#333"/></svg>
  </div>
  <div class="abs info-text" style="top:85px">415 Harbor Lane, Suite 210<br>Clearwater, FL 33755, United States</div>
  <div class="abs info-icon" style="top:117px">
    <svg width="12" height="9" viewBox="0 0 12 9"><rect width="12" height="9" rx="1" fill="#fff"/><polyline points="0.5,1 6,5 11.5,1" fill="none" stroke="#333" stroke-width="1"/></svg>
  </div>
  <div class="abs info-text" style="top:122px">info@veltrocheck.com</div>
  <div class="abs info-icon" style="top:153px">
    <svg width="11" height="11" viewBox="0 0 11 11"><path d="M2 0.5 L4 3 L3 4.5 C3.7 6 5 7.3 6.5 8 L8 7 L10.5 9 L9 10.5 C5 10.5 0.5 6 0.5 2 Z" fill="#fff"/></svg>
  </div>
  <div class="abs info-text" style="top:158px">1 - 555 - 240 - 7310</div>

  <div class="abs sub-title" style="left:457px;top:189px">SOCIAL</div>
  <div class="abs social-box" style="left:458px"></div>
  <div class="abs social-box" style="left:481px"></div>
  <div class="abs social-box" style="left:504px"></div>
  <div class="abs social-box" style="left:527px"></div>
</section>

<footer class="abs copyright">Copyrights © 2016, VeltroCheck . All Rights Reserved.</footer>

</body>
</html>
```